Consulting Practice for Charities Needs A Brochure Deisgn

Hi! We need a tri-fold brochure for a Washington, DC based consulting practice that works with charities (NGOs, Associations, etc.) and wealthy donors (philanthropists). Our company, Morrow Civic Advisors, helps nonprofits to implement practices that maximize organizational efficiency and effectiveness - by working directly with board members and staff.
Our clients are well educated and quite sophisticated (some charities are international with multi-million dollar budgets, while others are quite local and small) This brochure will be handed to them by some of our 'referral partners' (law firms, accountants and even governmental agencies) in addition to being given out during our presentations. We draw inspiration from nature and would like to somehow include a "natural / eco-friendly" feel to the piece, including natural colors .... that being said, not in any way "folksy" - it must be sophisticated.

Target Market(s)

nonprofit executive directors, board chairs, wealth holders (philanthropists)

Industry/Entity Type

Consulting

Requirements
Must have
• I uploaded a word file with content (text) - most of that needs to be on the brochure ... but ... if it looks too crowded, let me know and I'll reduce
Nice to have
• pop-out quotes (maybe from testimonials??), nature - theme of some kind but also photo of boardroom (links to samples are like are uploaded in a word doc below)
Should not have
• nothing cute ... nothing too feminine

```html
<!DOCTYPE html>
<html lang="en">
<head>
<meta charset="utf-8">
<title>Morrow Civic Advisors – Tri-fold Brochure</title>
<link href="https://fonts.googleapis.com/css2?family=Questrial&display=swap" rel="stylesheet">
<style>
  :root {
    --green-dark: #3f8f3a;
    --green-mid: #6fae5c;
    --green-light: #cfe4c2;
    --green-pale: #e6f1de;
    --orange: #d8622c;
    --gold: #c9b26a;
    --ink: #1c1c1c;
    --paper: #ffffff;
  }
  * { box-sizing: border-box; margin: 0; padding: 0; }
  html, body { width: 1200px; height: 848px; overflow: hidden; background: var(--paper); }
  body { font-family: "Questrial", "Century Gothic", sans-serif; color: var(--ink); }

  .brochure { position: relative; width: 1200px; height: 848px; overflow: hidden; background: var(--paper); }

  .swoosh { position: absolute; left: 0; width: 1200px; z-index: 2; pointer-events: none; }
  .swoosh--top { top: 0; height: 180px; }
  .swoosh--bottom { bottom: 0; height: 140px; }

  .photo { position: absolute; z-index: 1; }
  .photo--team { left: 405px; top: 56px; width: 399px; height: 260px;
    background: linear-gradient(180deg, #e9edf0 0%, #b9c1c8 55%, #6e7378 100%); }
  .photo--meeting { left: 0; top: 552px; width: 404px; height: 296px;
    background: linear-gradient(160deg, #dfe5ea 0%, #9ea8b2 50%, #3b4250 100%); }
  .photo--review { left: 804px; top: 512px; width: 396px; height: 240px;
    background: linear-gradient(120deg, #f2f2f2 0%, #cdd2d8 45%, #2f3a52 100%); }

  .heading {
    position: absolute; z-index: 3; height: 32px;
    background: var(--green-light); border-radius: 10px;
    box-shadow: 2px 3px 3px rgba(0,0,0,.25);
    font-size: 18px; line-height: 32px; padding-left: 120px;
  }
  .heading__mark {
    position: absolute; width: 40px; height: 40px; border-radius: 50%;
    background: var(--green-mid); left: 28px; top: -26px;
  }
  .heading--who { left: 44px; top: 98px; width: 344px; padding-left: 118px; }
  .heading--what { left: 434px; top: 342px; width: 344px; padding-left: 118px; }
  .heading--services { left: 833px; top: 98px; width: 343px; padding-left: 118px; }

  .tag {
    position: absolute; z-index: 3; background: var(--orange); color: #fff;
    border-radius: 10px; box-shadow: 2px 3px 3px rgba(0,0,0,.25);
    text-align: center; font-size: 13.2px; line-height: 15.5px;
    display: flex; flex-direction: column; justify-content: center;
  }

  .copy { position: absolute; z-index: 3; font-size: 12.8px; line-height: 15.4px; }
  .copy--center { text-align: center; }

  .label { position: absolute; z-index: 3; font-size: 12.6px; line-height: 15.4px; display: flex; gap: 10px; }
  .label__dot { width: 16px; height: 16px; border-radius: 50%; background: var(--green-mid); flex: none; margin-top: -4px; }

  .list { list-style: none; }
  .list li::before { content: "• "; }
</style>
</head>
<body>
<main class="brochure">

  <svg class="swoosh swoosh--top" viewBox="0 0 1200 180" preserveAspectRatio="none" aria-hidden="true">
    <path d="M0 48 C300 10 700 5 1200 30 L1200 96 C850 40 420 60 0 168 Z" fill="var(--green-mid)"/>
    <path d="M0 48 C300 10 700 5 1200 30 L1200 46 C820 20 380 30 0 70 Z" fill="var(--green-dark)"/>
  </svg>

  <div class="photo photo--team" role="img" aria-label="Photo of a smiling group of five business professionals standing together"></div>
  <div class="photo photo--meeting" role="img" aria-label="Photo of colleagues shaking hands across a meeting table"></div>
  <div class="photo photo--review" role="img" aria-label="Photo of two professionals reviewing documents together"></div>

  <svg class="swoosh swoosh--bottom" viewBox="0 0 1200 140" preserveAspectRatio="none" aria-hidden="true">
    <path d="M0 44 C380 100 780 90 1200 0 L1200 140 L0 140 Z" fill="var(--green-mid)"/>
    <path d="M0 90 C400 140 800 120 1200 50 L1200 140 L0 140 Z" fill="var(--green-dark)"/>
    <path d="M0 112 C400 150 800 140 1200 100 L1200 140 L0 140 Z" fill="var(--green-pale)" opacity=".6"/>
  </svg>

  <!-- Left panel -->
  <h2 class="heading heading--who"><span class="heading__mark"></span>Who We Are:</h2>
  <p class="copy copy--center" style="left:40px; top:148px; width:350px;">
    Founded in 2010 by Helen Marie Ashford, MCA was inspired by the national climate for stronger governance and deeper board engagement.&nbsp; Since then, we’ve worked with hundreds of board members to improve the impact of their philanthropic efforts. Our energetic and patient team of experts in nonprofit governance, operations and management will provide a comprehensive approach to problem solving, training and coaching.
  </p>
  <div class="tag" style="left:82px; top:298px; width:266px; height:54px;">
    <span>THE RESULT?</span>
    <span>- Better Boards - Stronger Organizations</span>
    <span>- Greater Impact</span>
  </div>
  <p class="label" style="left:100px; top:378px;"><span class="label__dot"></span>MCA CONSULTANTS WILL:</p>
  <ul class="copy list" style="left:42px; top:409px; width:330px;">
    <li>Bring new perspectives and skills for strategic or generative (big picture) thinking</li>
    <li>Challenge your assumptions</li>
    <li>Offer innovative approaches to problem solving</li>
    <li>Identify sources of dysfunction</li>
    <li>Devise tactics to improve decision making or communication</li>
    <li>Make breakthrough improvements</li>
  </ul>

  <!-- Middle panel -->
  <h2 class="heading heading--what"><span class="heading__mark"></span>What We Do:</h2>
  <div class="tag" style="left:494px; top:393px; width:226px; height:31px;">ORGANIZATIONAL CLIENTS</div>
  <p class="copy copy--center" style="left:440px; top:447px; width:334px;">
    20th century developmental psychologist Martin Ellsworth asserted that for individuals, conflict and crisis are positive and necessary; they are "sources of growth, strength, and commitment."<br>
    We believe the same can be true of organizations. MCA helps nonprofits manage change and emerge triumphantly.&nbsp; Through coaching, we help organizations implement practices to maximize efficiency and effectiveness - whether preparing for transition, coping with chaos, or simply pursuing continued high performance - by working directly with board members and staff.<br>
    Our methods are informed by research and honed by over 20 years of practice.
  </p>
  <div class="tag" style="left:494px; top:684px; width:226px; height:31px;">PRIVATE CLIENTS</div>
  <p class="copy copy--center" style="left:440px; top:738px; width:334px;">
    MCA philanthropic counsel helps individuals adopt impactful practices in their charitable endeavors.
  </p>

  <!-- Right panel -->
  <h2 class="heading heading--services"><span class="heading__mark"></span>Our Services:</h2>
  <div class="tag" style="left:865px; top:151px; width:275px; height:31px;">BOARD AND SENIOR STAFF COACHING</div>
  <p class="label" style="left:872px; top:205px; text-align:center;"><span class="label__dot"></span><span>WORKSHOPS, SEMINARS AND<br>RETREATS INCLUDING:</span></p>
  <ul class="copy copy--center list" style="left:850px; top:251px; width:310px;">
    <li>Roles &amp; Responsibilities</li>
    <li>Fundraising</li>
    <li>Succession Planning</li>
    <li>Board Self-Assessments</li>
    <li>Strategic Planning</li>
    <li>Board Recruitment Training</li>
    <li>Communications Development</li>
    <li>Grassroots Advocacy</li>
    <li>Mergers &amp; Acquisitions</li>
  </ul>
  <div class="tag" style="left:851px; top:411px; width:303px; height:79px;">
    <span>PHILANTHROPIC COUNSEL</span>
    <span>BOARD PLACEMENT</span>
    <span>BOARD MEMBER RECRUITMENT</span>
    <span>BOARD RETREAT PLANNING &amp; FACILITATION</span>
  </div>

</main>
</body>
</html>
```